Summit Reach Marketing
"Lifting your Brand Plans Past Every Limit"
Summit Reach Marketing - Marketing
Creative Brief
Use same font as used in my logo
Berlin
Professional
Nadia Kfoury
Marketing Consultant
Summit Reach Marketing T 961 1 847063 F 961 1 847063 M 961 3 402815 Po.Box: 738419 Beirut W http://www.summitreachmkt.me E nadiak@summitreachmkt.me E sales@summitreachmkt.me E info@summitreachmkt.me UAE | LEBANON | Summit Reach Marketing ... Lifting your Brand Plans Past Every Limit
nadia@summitreachmkt.me
on the back of the business card i want it to be in a form that ables someone to write additional notes. I maybe suggest it to be done in a form of a postcard. I suggest you check out www.summitreachmkt.me to see the spirit of the company and colors

```html
<!DOCTYPE html>
<html lang="en">
<head>
<meta charset="utf-8">
<title>Summit Reach Marketing – Stationery Set</title>
<link href="https://fonts.googleapis.com/css2?family=Montserrat:wght@400;600;700&display=swap" rel="stylesheet">
<style>
:root{
  --brand-red:#a3172a;
  --brand-red-dark:#7e0f1f;
  --paper:#ffffff;
  --paper-shade:#f1eeee;
  --ink:#4a4a4a;
  --rule:#d9d2d3;
  --stage:#e6e4e1;
}
*{margin:0;padding:0;box-sizing:border-box}
html,body{width:1200px;height:655px;overflow:hidden}
body{background:var(--stage);font-family:"Montserrat",Arial,sans-serif;color:var(--ink);position:relative}
.piece{position:absolute;background:var(--paper);overflow:hidden;box-shadow:0 2px 6px rgba(0,0,0,.18)}
.piece svg.swoosh{position:absolute;left:0;width:100%;display:block}
.brand{display:flex;align-items:center;gap:5px;position:absolute;white-space:nowrap}
.brand .dot{width:14px;height:14px;border-radius:50%;background:var(--brand-red);flex:none}
.brand .name{font-weight:700;color:var(--brand-red);font-size:8px;letter-spacing:.3px;text-transform:uppercase}
.contact{position:absolute;font-size:5px;line-height:1.55;color:var(--ink);white-space:nowrap}

/* business card front */
.card-front{left:53px;top:60px;width:206px;height:113px}
.card-front .brand{left:12px;top:16px}
.card-front .person{position:absolute;left:14px;top:50px}
.card-front .person b{display:block;font-size:7px;font-weight:600}
.card-front .person span{font-size:5px}
.card-front .contact{left:108px;top:38px}

/* notes card */
.card-notes{left:53px;top:185px;width:206px;height:120px}
.card-notes .lines{position:absolute;left:14px;right:14px;top:46px}
.card-notes .lines i{display:block;height:15px;border-bottom:1px solid var(--rule)}

/* red card */
.card-red{left:271px;top:60px;width:209px;height:120px;background:var(--brand-red)}
.card-red .emblem{position:absolute;left:50%;top:26px;width:34px;height:34px;margin-left:-17px;border-radius:50%;background:var(--paper)}
.card-red .name{position:absolute;left:0;right:0;top:68px;text-align:center;font-weight:700;font-size:8px;letter-spacing:.3px;color:var(--paper);text-transform:uppercase}
.card-red .tagline{position:absolute;left:0;right:0;top:86px;text-align:center;font-size:5px;color:var(--paper)}
.card-red .url{position:absolute;left:0;right:0;top:94px;text-align:center;font-size:5px;color:var(--paper)}

/* logo card */
.card-logo{left:271px;top:185px;width:209px;height:120px}
.card-logo .emblem{position:absolute;left:50%;top:20px;width:30px;height:30px;margin-left:-15px;border-radius:50%;background:var(--brand-red)}
.card-logo .name{position:absolute;left:0;right:0;top:58px;text-align:center;font-weight:700;font-size:8px;color:var(--brand-red);text-transform:uppercase;letter-spacing:.3px}

/* envelope front */
.envelope{left:132px;top:365px;width:368px;height:139px}
.envelope .brand{left:18px;top:18px}
.envelope .contact{left:198px;top:14px}

/* letterhead */
.letterhead{left:499px;top:65px;width:305px;height:391px}
.letterhead .brand{left:18px;top:16px}
.letterhead .contact{left:190px;top:12px}

/* envelope back */
.envelope-back{left:487px;top:463px;width:317px;height:142px;background:var(--paper-shade)}
.envelope-back .seal{position:absolute;left:50%;top:50px;width:28px;height:28px;margin-left:-14px;border-radius:50%;background:var(--paper)}

/* fax sheet */
.fax-sheet{left:823px;top:65px;width:305px;height:396px}
.fax-sheet .brand{left:18px;top:16px}
.fax-sheet .contact{left:190px;top:12px}
.fax-form{position:absolute;left:18px;right:18px;top:84px;display:grid;grid-template-columns:1fr 1fr;column-gap:14px;row-gap:6px;font-size:5px}
.fax-form div{border-bottom:1px solid var(--rule);padding-bottom:2px}
.fax-form .wide{grid-column:1 / 3}
.fax-sheet .comments{position:absolute;left:18px;top:156px;font-size:5px}
</style>
</head>
<body>

<!-- Business card front -->
<section class="piece card-front">
  <svg class="swoosh" style="top:0;height:30px" viewBox="0 0 206 30" preserveAspectRatio="none"><path d="M0 0H206V4C140 4 70 10 0 26Z" fill="var(--brand-red)"/></svg>
  <div class="brand"><span class="dot"></span><span class="name">Summit Reach Marketing</span></div>
  <div class="person"><b>Nadia Kfoury</b><span>Marketing Consultant</span></div>
  <div class="contact">T 961 1 847063<br>M 961 3 402815<br>Po.Box: 738419 Beirut<br>nadiak@summitreachmkt.me<br>www.summitreachmkt.me</div>
  <svg class="swoosh" style="bottom:0;height:26px" viewBox="0 0 206 26" preserveAspectRatio="none"><path d="M0 26V22C70 22 140 16 206 0V26Z" fill="var(--brand-red)"/></svg>
</section>

<!-- Business card back: notes -->
<section class="piece card-notes">
  <svg class="swoosh" style="top:0;height:36px" viewBox="0 0 206 36" preserveAspectRatio="none"><path d="M206 0H120C150 8 180 22 206 34Z" fill="var(--brand-red)"/></svg>
  <div class="lines"><i></i><i></i><i></i><i></i></div>
</section>

<!-- Red card -->
<section class="piece card-red">
  <span class="emblem"></span>
  <div class="name">Summit Reach Marketing</div>
  <div class="tagline">"Lifting your Brand Plans Past Every Limit"</div>
  <div class="url">http://www.summitreachmkt.me</div>
</section>

<!-- Logo card -->
<section class="piece card-logo">
  <span class="emblem"></span>
  <div class="name">Summit Reach Marketing</div>
  <svg class="swoosh" style="bottom:0;height:34px" viewBox="0 0 209 34" preserveAspectRatio="none"><path d="M209 34H90C140 30 180 18 209 0Z" fill="var(--brand-red)"/></svg>
</section>

<!-- Envelope front -->
<section class="piece envelope">
  <div class="brand"><span class="dot"></span><span class="name">Summit Reach Marketing</span></div>
  <div class="contact">Po.Box: 738419 Beirut<br>T 961 1 847063<br>F 961 1 847063<br>E info@summitreachmkt.me<br>W www.summitreachmkt.me</div>
  <svg class="swoosh" style="bottom:0;height:60px" viewBox="0 0 368 60" preserveAspectRatio="none"><path d="M0 60V10C120 40 260 44 368 24V60Z" fill="var(--brand-red)"/><path d="M0 10C120 40 260 44 368 24V30C260 50 120 48 0 18Z" fill="var(--brand-red-dark)"/></svg>
</section>

<!-- Letterhead -->
<section class="piece letterhead">
  <div class="brand"><span class="dot"></span><span class="name">Summit Reach Marketing</span></div>
  <div class="contact">Po.Box: 738419 Beirut<br>T 961 1 847063<br>F 961 1 847063<br>E info@summitreachmkt.me<br>W www.summitreachmkt.me</div>
  <svg class="swoosh" style="bottom:0;height:70px" viewBox="0 0 305 70" preserveAspectRatio="none"><path d="M0 70V30C100 50 210 46 305 0V70Z" fill="var(--brand-red)"/><path d="M0 22C100 44 210 40 305 0V8C210 48 100 52 0 30Z" fill="var(--paper-shade)"/></svg>
</section>

<!-- Envelope back -->
<section class="piece envelope-back">
  <svg class="swoosh" style="top:0;height:100%" viewBox="0 0 317 142" preserveAspectRatio="none"><path d="M0 0H317L158 92Z" fill="var(--brand-red)"/><path d="M0 0L158 92L317 0V8L158 100L0 8Z" fill="var(--brand-red-dark)"/></svg>
  <span class="seal"></span>
</section>

<!-- Fax sheet -->
<section class="piece fax-sheet">
  <div class="brand"><span class="dot"></span><span class="name">Summit Reach Marketing</span></div>
  <div class="contact">Po.Box: 738419 Beirut<br>T 961 1 847063<br>F 961 1 847063<br>E sales@summitreachmkt.me<br>W www.summitreachmkt.me</div>
  <div class="fax-form">
    <div>To:</div><div>From:</div>
    <div>Fax:</div><div>Pages:</div>
    <div>Phone:</div><div>Date:</div>
    <div class="wide">Subject:</div>
  </div>
  <div class="comments">Comments:</div>
  <svg class="swoosh" style="bottom:0;height:70px" viewBox="0 0 305 70" preserveAspectRatio="none"><path d="M0 70V30C100 50 210 46 305 0V70Z" fill="var(--brand-red)"/><path d="M0 22C100 44 210 40 305 0V8C210 48 100 52 0 30Z" fill="var(--paper-shade)"/></svg>
</section>

</body>
</html>
```